Kestrel Building Works Business Card and more!

We need a business card design for Kestrel Building Works Ltd, a respected building company that specialises in high quality designer homes.

We're after a sleek, clean, modern business card that incorporates our new logo (see attached) and colours, with black being the background.

We are Certified Framing Guild and need to include their logo (see attached) on our cards, balancing but not taking over our logo.

Details to be included:

Malcolm Tivey
Director

Phone: 0218845126
Email: kestrelbuild.nz@maildrop-example.co.nz
Website: www.kestrelbuildingworks-example.co.nz

Additional Information

A start up website is also under construction and needing attention and letterheads are needed!

We look forward to your designs!

Target Market(s)

30+ people who are interested in building new or renovating current homes

Industry/Entity Type

Construction

Contact Information for Business Card

Malcolm Tivey
Director

Phone: 0218845126
Facebook: www.socialpage-example.com/kestrelbuild.nz

Font styles to use
Serif

Colors

Designer to choose colors to be used in the design.

Requirements
Must have
• Our new logo
• Our colours
• cfg logo

```html
<!DOCTYPE html>
<html lang="en">
<head>
<meta charset="utf-8">
<title>Kestrel Building Works – Business Card</title>
<link href="https://fonts.googleapis.com/css2?family=Cinzel:wght@400;600&family=Open+Sans:wght@400;600&display=swap" rel="stylesheet">
<style>
  :root {
    --backdrop: #3b3b3b;
    --card: #0c0c0c;
    --card-edge: #1a1a1a;
    --pattern-light: #1c1c1c;
    --pattern-dark: #0a0a0a;
    --white: #f4f2ee;
    --gold: #c9924a;
    --grey: #bdbdbd;
  }
  * { box-sizing: border-box; margin: 0; padding: 0; }
  html, body {
    width: 1200px;
    height: 765px;
    overflow: hidden;
    background: var(--backdrop);
  }
  .canvas {
    position: relative;
    width: 1200px;
    height: 765px;
    display: flex;
    align-items: center;
    justify-content: center;
    gap: 50px;
  }
  .card {
    position: relative;
    width: 520px;
    height: 316px;
    background: var(--card);
    border: 1px solid var(--card-edge);
    box-shadow: 0 18px 40px rgba(0,0,0,0.35);
    overflow: hidden;
  }

  /* Front */
  .card-front__pattern {
    position: absolute;
    inset: 0;
    background: linear-gradient(135deg, var(--pattern-light) 0%, var(--pattern-dark) 55%, var(--pattern-light) 100%);
  }
  .brand-lockup {
    position: absolute;
    left: 50%;
    top: 50%;
    transform: translate(-50%, -50%);
    display: flex;
    flex-direction: column;
    align-items: center;
    gap: 14px;
  }
  .brand-lockup__dot {
    width: 34px;
    height: 34px;
    border-radius: 50%;
    background: var(--gold);
  }
  .brand-lockup__name {
    font-family: "Cinzel", serif;
    font-weight: 600;
    font-size: 30px;
    letter-spacing: 2px;
    color: var(--white);
    text-align: center;
    line-height: 1.15;
  }

  /* Back */
  .card-back__brand {
    position: absolute;
    left: 40px;
    top: 44px;
    display: flex;
    align-items: center;
    gap: 12px;
  }
  .card-back__brand .brand-lockup__dot {
    width: 24px;
    height: 24px;
  }
  .card-back__brand-name {
    font-family: "Cinzel", serif;
    font-weight: 600;
    font-size: 20px;
    letter-spacing: 1.5px;
    color: var(--white);
  }
  .person {
    position: absolute;
    left: 40px;
    top: 140px;
  }
  .person__name {
    font-family: "Cinzel", serif;
    font-weight: 400;
    font-size: 22px;
    letter-spacing: 1px;
    color: var(--white);
  }
  .person__role {
    font-family: "Open Sans", sans-serif;
    font-weight: 600;
    font-size: 10px;
    letter-spacing: 1px;
    color: var(--white);
    margin-top: 4px;
  }
  .contact {
    position: absolute;
    left: 40px;
    top: 208px;
    padding-left: 12px;
    border-left: 2px solid var(--gold);
    list-style: none;
    font-family: "Open Sans", sans-serif;
    font-size: 10.5px;
    line-height: 16px;
    color: var(--grey);
  }
  .guild-badge {
    position: absolute;
    right: 40px;
    top: 128px;
    width: 66px;
    height: 66px;
    border-radius: 50%;
    background: var(--white);
  }
</style>
</head>
<body>
  <main class="canvas">
    <section class="card card-front">
      <div class="card-front__pattern" role="img" aria-label="Faint repeating brand mark pattern in dark tones"></div>
      <div class="brand-lockup">
        <span class="brand-lockup__dot"></span>
        <p class="brand-lockup__name">Kestrel<br>Building Works</p>
      </div>
    </section>

    <section class="card card-back">
      <div class="card-back__brand">
        <span class="brand-lockup__dot"></span>
        <p class="card-back__brand-name">Kestrel Building Works</p>
      </div>

      <div class="person">
        <p class="person__name">Malcolm Tivey</p>
        <p class="person__role">DIRECTOR</p>
      </div>

      <ul class="contact">
        <li>0218845126</li>
        <li>kestrelbuild.nz@maildrop-example.co.nz</li>
        <li>www.kestrelbuildingworks-example.co.nz</li>
        <li>www.socialpage-example.com/kestrelbuild.nz</li>
      </ul>

      <div class="guild-badge" role="img" aria-label="Certified Framing Guild membership badge"></div>
    </section>
  </main>
</body>
</html>
```